Design a Single Fold Brochure for Q7R Consulting

Hello i have this small project for you.
I will like to have a single fold brochure designed for a a small start up: Q7R Consulting.
I have attached a zip files containing logo and business cards you may use for the aim of this project. You my also dsigned a different brochure style which will match with the company's logo color
I will like the brochures to come along with illustration images as well as an appropriate design which represent the business activities.

The info to enter in the brochure are:

-Industrial Development and Public Works: In 2014, Q7R consulting has lead one of the biggest construction company in the world to financing and securing business oportunities in most Central African Countries like Gabon, Chad etc.

-Support and Investment Missions: Q7r has accompanied several big projects within various industrial sectors from international companies which has ongoing investments in Cameroon, Gabon , Chad and other African countries.

-Business Lobbying: Q7r bridges the socio-cultural and developmental gap between foreign business owners and local businesses by easing economic exchanges and enhancing small business growth in the various industries

-International Representations: International companies and group can benefit of contact facilitation and representation through Q7R experienced business leaders. Today Q7R is representing several businesses from China, Switzerland, France in most African Countries.

-New Technology Development and Commercialization: Today Q7R Consulting is commercializing several newly developped technologies in most African Countries

CONTACT:

Q7R Consulting USA
Address: 2286 Larkwood Ave, Suite 518 - B
Wilmington, DE
19842 USA
Phone: 22222222

Q7R Consulting Cameroon
Address: Douala - Cameroon
Phone: 237 654 219 847

Website: www.q7rconsulting.example
email: info@q7rconsulting.example

```html
<!DOCTYPE html>
<html lang="en">
<head>
<meta charset="utf-8">
<title>Q7R Consulting – Single Fold Brochure</title>
<link href="https://fonts.googleapis.com/css2?family=Electrolize&display=swap" rel="stylesheet">
<style>
  :root {
    --stage: #8c8c8c;
    --paper-light: #f4f4f4;
    --paper-mid: #d9d9d9;
    --paper-dark: #b9b9b9;
    --band-grey: #6f6f70;
    --band-black: #0a0a0a;
    --magenta: #b0197e;
    --ink-grey: #6d6e70;
  }
  * { box-sizing: border-box; margin: 0; padding: 0; }
  html, body { width: 1200px; height: 1020px; overflow: hidden; }
  body {
    background: var(--stage);
    font-family: "Electrolize", "Trebuchet MS", sans-serif;
    position: relative;
  }

  /* ---------- Outside spread (back + front cover) ---------- */
  .outside-spread {
    position: absolute;
    left: 130px; top: 40px;
    width: 940px; height: 420px;
    display: flex;
  }
  .panel {
    position: relative;
    width: 50%;
    height: 100%;
    overflow: hidden;
  }
  .panel--back { background: linear-gradient(90deg, var(--paper-mid) 0%, var(--paper-light) 100%); }
  .panel--front { background: linear-gradient(90deg, var(--paper-light) 0%, var(--paper-mid) 100%); }

  .panel__stripe {
    position: absolute; left: 0; right: 0;
    top: 290px; height: 22px;
    background: linear-gradient(180deg, #9a9a9a, var(--band-grey));
  }
  .panel__band {
    position: absolute; left: 0; right: 0; bottom: 0;
    top: 312px;
    background: var(--band-black);
    color: var(--magenta);
  }

  .contact {
    position: absolute;
    left: 16px; top: 90px;
    color: var(--magenta);
    font-size: 13px;
    line-height: 1.6;
  }
  .contact__block + .contact__block { margin-top: 20px; }
  .web-contact {
    padding: 26px 0 0 16px;
    font-size: 14px;
    line-height: 1.6;
  }

  .brand {
    position: absolute;
    left: 28px; top: 100px;
    display: flex; align-items: center; gap: 12px;
  }
  .brand__square {
    width: 22px; height: 22px;
    background: var(--magenta);
  }
  .brand__name {
    font-size: 48px;
    color: var(--magenta);
    letter-spacing: 1px;
    line-height: 1;
  }
  .tagline {
    position: absolute;
    left: 62px; top: 160px;
    font-size: 17px;
    color: var(--ink-grey);
  }
  .service-icons {
    position: absolute;
    left: 40px; top: 205px;
    width: 400px; height: 60px;
    background: linear-gradient(90deg, #a9a9a9, #c7c7c7, #a9a9a9);
    border-radius: 4px;
  }
  .front-headline {
    text-align: right;
    padding: 36px 22px 0 0;
    font-size: 17px;
    letter-spacing: 0.5px;
  }

  /* ---------- Inside spread ---------- */
  .inside-spread {
    position: absolute;
    left: 60px; top: 545px;
    width: 1080px; height: 435px;
    display: flex;
  }
  .inside-panel {
    position: relative;
    width: 50%; height: 100%;
    background: linear-gradient(180deg, #ededed 0%, var(--paper-dark) 100%);
    border-right: 1px solid #c9c9c9;
  }
  .inside-panel:last-child { border-right: none; border-left: 1px solid #fafafa; }
  .triangle-field {
    position: absolute;
    left: 0; right: 0; top: 20px; height: 320px;
    background: radial-gradient(ellipse at 50% 50%, rgba(120,120,120,0.35) 0%, rgba(150,150,150,0.12) 55%, rgba(200,200,200,0) 80%);
  }
  .inside-copy {
    position: absolute;
    left: 22px; right: 22px;
    color: var(--magenta);
    font-size: 13.4px;
    line-height: 1.6;
  }
  .inside-copy p + p { margin-top: 20px; }
  .inside-panel--left .inside-copy { top: 110px; }
  .inside-panel--right .inside-copy { top: 82px; }
  .inside-footer {
    position: absolute; left: 0; right: 0; bottom: 0;
    height: 36px;
    background: var(--band-black);
    border-top: 6px solid var(--band-grey);
    display: flex; align-items: center; justify-content: center;
  }
  .inside-footer__name {
    color: var(--magenta);
    font-size: 20px;
    letter-spacing: 1px;
  }
</style>
</head>
<body>

<section class="outside-spread" aria-label="Brochure outside: back and front cover">
  <div class="panel panel--back">
    <div class="contact">
      <div class="contact__block">
        Q7R Consulting USA<br>
        Address: 2286 Larkwood Ave, Suite 518 - B<br>
        Wilmington, DE<br>
        19842 USA<br>
        Phone: 22222222
      </div>
      <div class="contact__block">
        Q7R Consulting Cameroon<br>
        Address: Douala - Cameroon<br>
        Phone: 237 654 219 847
      </div>
    </div>
    <div class="panel__stripe"></div>
    <div class="panel__band">
      <div class="web-contact">
        Website: www.q7rconsulting.example<br>
        email: info@q7rconsulting.example
      </div>
    </div>
  </div>

  <div class="panel panel--front">
    <div class="brand">
      <span class="brand__square"></span>
      <span class="brand__name">Q7R Consulting</span>
    </div>
    <div class="tagline">Trusted Partners for Growth in Africa</div>
    <div class="service-icons" role="img" aria-label="Row of six grey pictograms showing growth, planning, finance, teamwork, advice and meetings"></div>
    <div class="panel__stripe"></div>
    <div class="panel__band">
      <div class="front-headline">New Technology Development and Commercialization</div>
    </div>
  </div>
</section>

<section class="inside-spread" aria-label="Brochure inside spread">
  <div class="inside-panel inside-panel--left">
    <div class="triangle-field" role="img" aria-label="Scattered grey triangle shards decoration"></div>
    <div class="inside-copy">
      <p>Industrial Development and Public Works: In 2014, Q7R consulting has lead one of the biggest construction company in the world to financing and securing business oportunities in most Central African Countries like Gabon, Chad etc.</p>
      <p>Support and Investment Missions: Q7r has accompanied several big projects within various industrial sectors from international companies which has ongoing investments in Cameroon, Gabon , Chad and other African countries.</p>
    </div>
    <div class="inside-footer"><span class="inside-footer__name">Q7R</span></div>
  </div>

  <div class="inside-panel inside-panel--right">
    <div class="triangle-field" role="img" aria-label="Scattered grey triangle shards decoration"></div>
    <div class="inside-copy">
      <p>Business Lobbying: Q7r bridges the socio-cultural and developmental gap between foreign business owners and local businesses by easing economic exchanges and enhancing small business growth in the various industries.</p>
      <p>International Representations: International companies and group can benefit of contact facilitation and representation through Q7R experienced business leaders. Today Q7R is representing several businesses from China, Switzerland, France in most African Countries.</p>
      <p>New Technology Development and Commercialization: Today Q7R Consulting is commercializing several newly developped technologies in most African Countries.</p>
    </div>
    <div class="inside-footer"><span class="inside-footer__name">Q7R</span></div>
  </div>
</section>

</body>
</html>
```